Cradle Glow Events

New Company ,I will attened clients personal residents(venu of there choice) and provide 3D ultra sound photos at time of ultra sound.This is a Non diagnostic ultra sound which does not replace the ultrasound reqested by Dr.The best time for ultra sound is 24 to 34 weeks.The baby sex can be kept confidential if requied and all cultral and diverse backgrounds cattered for..No referal requied for this.I have 2 main packges,1 baby shower and 2 family time.Extra options available are entertainment,Family time prior to baby shower for dad,decoration, Kids entertainment.
Contact number is 0471938402 email to be added ASAP.
prices start from $450

It Company

```html
<!DOCTYPE html>
<html lang="en">
<head>
<meta charset="utf-8">
<title>Cradle Glow Events – 3D ultra sound photos</title>
<link href="https://fonts.googleapis.com/css2?family=Architects+Daughter&family=Jost:wght@400;500;600&display=swap" rel="stylesheet">
<style>
  :root {
    --title-red: #e62a2a;
    --ink: #111111;
    --body-ink: #1a1a1a;
    --skin-light: #f3c9b3;
    --skin-mid: #e7a88c;
    --skin-deep: #c98266;
    --paper: #e9e0cc;
    --paper-edge: #d9ccb2;
    --card-orange: #ef4423;
    --card-magenta: #b21f6e;
    --price-pink: #e8185e;
    --brand-pink: #d91f6e;
    --icon-pink: #c2185b;
    --white: #ffffff;
  }
  * { margin: 0; padding: 0; box-sizing: border-box; }
  html, body { width: 1200px; height: 848px; overflow: hidden; background: var(--white); }
  .flyer {
    position: relative;
    width: 1200px;
    height: 848px;
    overflow: hidden;
    background: var(--white);
    font-family: "Jost", sans-serif;
    color: var(--ink);
  }
  .belly-photo {
    position: absolute;
    left: 0; top: 0;
    width: 650px; height: 848px;
    background:
      radial-gradient(ellipse 340px 400px at 300px 430px, var(--skin-light) 0%, var(--skin-mid) 60%, rgba(231,168,140,0) 100%),
      linear-gradient(90deg, var(--skin-deep) 0%, var(--skin-mid) 45%, var(--white) 100%);
  }
  .headline {
    position: absolute;
    left: 558px; top: 2px;
    font-family: "Architects Daughter", cursive;
    font-size: 54px;
    font-weight: 400;
    color: var(--title-red);
    letter-spacing: 1px;
    white-space: nowrap;
  }
  .intro {
    position: absolute;
    left: 640px; top: 85px;
    width: 440px;
    font-family: "Architects Daughter", cursive;
    font-size: 20px;
    line-height: 22px;
    text-align: center;
    white-space: nowrap;
    color: var(--body-ink);
  }
  .package {
    position: absolute;
    width: 262px; height: 190px;
    padding: 12px;
    background: var(--paper);
    box-shadow: 0 0 0 2px var(--paper-edge), 2px 4px 8px rgba(0,0,0,0.25);
  }
  .package-face {
    width: 100%; height: 100%;
    display: flex;
    flex-direction: column;
    justify-content: center;
    align-items: center;
    color: rgba(255,255,255,0.82);
    font-weight: 500;
    line-height: 1.05;
  }
  .package-number { font-size: 25px; }
  .package-name { font-size: 38px; }
  .package--shower { left: 612px; top: 202px; transform: rotate(9deg); }
  .package--shower .package-face { background: var(--card-orange); }
  .package--family { left: 876px; top: 222px; transform: rotate(-12deg); }
  .package--family .package-face { background: var(--card-magenta); }
  .photo-corner { position: absolute; width: 30px; height: 30px; }
  .photo-corner--tl { left: -6px; top: -6px; }
  .photo-corner--tr { right: -6px; top: -6px; transform: rotate(90deg); }
  .photo-corner--br { right: -6px; bottom: -6px; transform: rotate(180deg); }
  .photo-corner--bl { left: -6px; bottom: -6px; transform: rotate(270deg); }
  .price-badge {
    position: absolute;
    left: 1006px; top: 362px;
    width: 96px; height: 96px;
    border-radius: 50%;
    background: var(--price-pink);
    color: var(--white);
    display: flex;
    flex-direction: column;
    align-items: center;
    justify-content: center;
  }
  .price-label { font-size: 7.5px; letter-spacing: 0.3px; margin-top: 6px; }
  .price-amount { font-size: 34px; font-weight: 500; line-height: 1; }
  .price-amount sup { font-size: 18px; vertical-align: 10px; }
  .extras {
    position: absolute;
    right: 28px; top: 485px;
    font-size: 16px;
    font-weight: 600;
    line-height: 22px;
    text-align: right;
    white-space: nowrap;
    color: var(--body-ink);
  }
  .disclaimer {
    position: absolute;
    left: 572px; top: 610px;
    width: 150px;
    font-size: 11px;
    font-weight: 600;
    line-height: 13.5px;
    text-align: center;
    color: var(--body-ink);
  }
  .brand {
    position: absolute;
    left: 812px; top: 568px;
    display: flex;
    align-items: center;
    gap: 14px;
  }
  .brand-dot { width: 22px; height: 22px; border-radius: 50%; background: var(--brand-pink); }
  .brand-name {
    font-size: 46px;
    font-weight: 500;
    line-height: 50px;
    color: var(--brand-pink);
    width: 300px;
  }
  .contact {
    position: absolute;
    left: 700px;
    display: flex;
    align-items: center;
    gap: 18px;
    color: var(--ink);
  }
  .contact--phone { top: 688px; }
  .contact--email { top: 770px; }
  .contact-phone-number { font-size: 62px; font-weight: 500; letter-spacing: 2px; }
  .contact-email-address { font-size: 47px; font-weight: 400; }
</style>
</head>
<body>
<main class="flyer">
  <div class="belly-photo" role="img" aria-label="Photo of a pregnant woman cradling her bare belly with both hands"></div>

  <h1 class="headline">3D ultra sound photos</h1>

  <p class="intro">The best time for a ultra sound is 24<br>to 34 weeks. The baby sex can be kept<br>confidential if required and all cultural<br>and diverse backgrounds catered for..<br>NO REFERAL REQUIED</p>

  <div class="package package--shower">
    <div class="package-face">
      <span class="package-number">Package #1</span>
      <span class="package-name">Baby Shower</span>
    </div>
    <svg class="photo-corner photo-corner--tl" viewBox="0 0 30 30" aria-hidden="true"><polygon points="0,0 30,0 0,30" fill="#1a1a1a"/></svg>
    <svg class="photo-corner photo-corner--tr" viewBox="0 0 30 30" aria-hidden="true"><polygon points="0,0 30,0 0,30" fill="#1a1a1a"/></svg>
    <svg class="photo-corner photo-corner--br" viewBox="0 0 30 30" aria-hidden="true"><polygon points="0,0 30,0 0,30" fill="#1a1a1a"/></svg>
    <svg class="photo-corner photo-corner--bl" viewBox="0 0 30 30" aria-hidden="true"><polygon points="0,0 30,0 0,30" fill="#1a1a1a"/></svg>
  </div>

  <div class="package package--family">
    <div class="package-face">
      <span class="package-number">Package #2</span>
      <span class="package-name">Family Time</span>
    </div>
    <svg class="photo-corner photo-corner--tl" viewBox="0 0 30 30" aria-hidden="true"><polygon points="0,0 30,0 0,30" fill="#1a1a1a"/></svg>
    <svg class="photo-corner photo-corner--tr" viewBox="0 0 30 30" aria-hidden="true"><polygon points="0,0 30,0 0,30" fill="#1a1a1a"/></svg>
    <svg class="photo-corner photo-corner--br" viewBox="0 0 30 30" aria-hidden="true"><polygon points="0,0 30,0 0,30" fill="#1a1a1a"/></svg>
    <svg class="photo-corner photo-corner--bl" viewBox="0 0 30 30" aria-hidden="true"><polygon points="0,0 30,0 0,30" fill="#1a1a1a"/></svg>
  </div>

  <div class="price-badge">
    <span class="price-label">PRICES START FROM</span>
    <span class="price-amount"><sup>$</sup>450</span>
  </div>

  <p class="extras">Extra options such as entertainment, Family time prior to baby<br>shower for dad,decoration, &amp; Kids entertainment are available.</p>

  <p class="disclaimer">*This is a Non diagnostic ultra sound which does not replace the ultrasound reqested by your Doctor</p>

  <div class="brand">
    <span class="brand-dot"></span>
    <span class="brand-name">Cradle Glow Events</span>
  </div>

  <div class="contact contact--phone">
    <svg width="44" height="48" viewBox="0 0 24 24" aria-hidden="true">
      <path fill="var(--icon-pink)" d="M6.6 10.8c1.4 2.8 3.8 5.1 6.6 6.6l2.2-2.2c.3-.3.7-.4 1-.2 1.1.4 2.3.6 3.6.6.6 0 1 .4 1 1V20c0 .6-.4 1-1 1C10.6 21 3 13.4 3 4c0-.6.4-1 1-1h3.5c.6 0 1 .4 1 1 0 1.3.2 2.5.6 3.6.1.3 0 .7-.2 1L6.6 10.8z"/>
    </svg>
    <span class="contact-phone-number">0471938402</span>
  </div>

  <div class="contact contact--email">
    <svg width="54" height="40" viewBox="0 0 54 40" aria-hidden="true">
      <rect x="2" y="2" width="50" height="36" fill="none" stroke="var(--icon-pink)" stroke-width="3"/>
      <polyline points="2,2 27,24 52,2" fill="none" stroke="var(--icon-pink)" stroke-width="3"/>
      <line x1="2" y1="38" x2="20" y2="19" stroke="var(--icon-pink)" stroke-width="3"/>
      <line x1="52" y1="38" x2="34" y2="19" stroke="var(--icon-pink)" stroke-width="3"/>
    </svg>
    <span class="contact-email-address">glow@mailbox.com</span>
  </div>
</main>
</body>
</html>
```